Web Design Project

We are re-starting this project.

This project is for a totally new look and design of a website for Wablor. www.wablor-demo.net.

Wablor is a naming protocol for physical locations and can be used for fixed and mobile people, places and things. Find your friends, or find a business. Because Wablor locations point to precise geo-physical (GPS) co-ordinates, navigation to a location becomes totally reliable.
Updates

Please see the modified brief for this project

Target Market(s)

Every person and every business can have multiple !Wabs (Wablor locations), so the website needs to be appealing and fun, but easy to use and functional

Industry/Entity Type

Business

Colors
34a6d7

Requirements
Must have
• Uniqueness!

```html
<!DOCTYPE html>
<html lang="en">
<head>
<meta charset="utf-8">
<title>Wablor – Find something or someone</title>
<link href="https://fonts.googleapis.com/css2?family=Ubuntu:wght@400;500;700&display=swap" rel="stylesheet">
<style>
  :root{
    --brand-blue:#34a6d7;
    --brand-blue-dark:#1b8fc4;
    --band-top:#3aa9dc;
    --band-bottom:#2d9ed3;
    --green:#7cc21e;
    --green-dark:#5fa40e;
    --ink:#4a4a4a;
    --ink-soft:#777;
    --panel:#f1f0f0;
    --panel-alt:#e6e5e5;
    --map:#e9e6df;
    --white:#fff;
  }
  *{box-sizing:border-box;margin:0;padding:0}
  html,body{width:1200px;height:1012px;overflow:hidden;background:var(--white);font-family:"Ubuntu",Arial,sans-serif;color:var(--ink)}
  .page{position:relative;width:1200px;height:1012px}
  .topline{position:absolute;left:0;top:0;width:1200px;height:3px;background:var(--brand-blue)}

  .brand{position:absolute;left:141px;top:28px;display:flex;align-items:center;gap:10px}
  .brand-dot{width:26px;height:26px;border-radius:50%;background:var(--brand-blue)}
  .brand-name{font-size:44px;font-weight:700;color:var(--brand-blue);letter-spacing:-1px}

  .main-nav{position:absolute;top:43px;left:518px;display:flex;gap:32px}
  .main-nav a{font-size:13.5px;font-weight:500;color:#555;text-decoration:none;letter-spacing:.3px}
  .btn{position:absolute;top:35px;height:32px;border-radius:7px;color:#fff;font-size:13.5px;font-weight:500;display:flex;align-items:center;justify-content:center}
  .btn-signup{left:904px;width:70px;background:linear-gradient(#2ba8e0,#1a8cc8)}
  .btn-login{left:989px;width:70px;background:linear-gradient(#86cc24,#5ea70f)}

  .search-band{position:absolute;left:0;top:113px;width:1200px;height:152px;background:linear-gradient(var(--band-top),var(--band-bottom))}
  .search-label{position:absolute;left:141px;top:24px;color:#fff;font-size:14px;font-weight:500}
  .field{position:absolute;top:55px;height:43px;width:216px;background:#fff;border:1px solid #d9e8ef;font-size:12px;color:#888;padding:13px 17px}
  .search-btn{position:absolute;left:515px;top:121px;width:169px;height:36px;border-radius:14px 14px 0 0;background:linear-gradient(#86cc24,#63aa10);color:#fff;font-size:15px;font-weight:500;display:flex;align-items:center;justify-content:center;z-index:2}

  .map{position:absolute;left:0;top:265px;width:1200px;height:652px;background:linear-gradient(135deg,#e8e4dc,#ecebe6 55%,#e3e6d8)}

  .results{position:absolute;left:142px;top:289px;width:244px;height:573px;background:var(--panel);border-radius:10px 10px 4px 4px;overflow:hidden;box-shadow:0 1px 3px rgba(0,0,0,.2)}
  .results-head{height:47px;background:linear-gradient(#86cc24,#68ae12);color:#fff;font-size:13.5px;font-weight:500;padding:16px 26px}
  .result{height:168px;padding:24px 24px 0 24px;width:230px}
  .result.alt{background:var(--panel-alt)}
  .result h3{font-size:13.5px;font-weight:500;color:#3b3b3b;margin-bottom:8px}
  .addr{font-size:11.5px;color:var(--ink-soft);margin-bottom:9px}
  .dist{font-size:11.5px;color:#333;display:flex;align-items:center;gap:10px}
  .instr{font-size:11.5px;color:var(--ink-soft);margin-top:28px}
  .links{display:flex;gap:8px;margin-top:8px;font-size:11.5px;color:var(--brand-blue-dark)}
  .links span{display:flex;align-items:center;gap:4px}
  .scrollbar{position:absolute;right:3px;top:54px;width:10px;height:508px;background:#fafafa;border-left:1px solid #ddd}
  .scroll-thumb{position:absolute;left:1px;top:14px;width:8px;height:100px;background:#d0d0d0;border-radius:3px}

  .map-pin{position:absolute;left:716px;top:471px}
  .popup{position:absolute;left:727px;top:553px;width:225px;height:127px;background:var(--brand-blue);border:6px solid #8fcbe8;color:#fff;padding:20px 18px}
  .popup h3{font-size:13.5px;font-weight:500;margin-bottom:11px}
  .popup .addr{color:#fff;margin-bottom:9px}
  .popup .dist{color:#fff}

  .map-controls{position:absolute;left:1097px;top:425px}

  .footer-nav{position:absolute;left:142px;top:943px;display:flex;font-size:12px;color:#444}
  .footer-nav span{padding:0 10px;border-right:1px solid #666;line-height:12px}
  .footer-nav span:first-child{padding-left:0}
  .footer-nav span:last-child{border-right:0}
  .copyright{position:absolute;left:140px;top:971px;font-size:11.5px;color:#444}
  .social{position:absolute;top:943px;left:843px;display:flex;gap:12px}
  .social i{display:block;width:40px;height:40px;border-radius:50%}
</style>
</head>
<body>
<div class="page">
  <div class="topline"></div>

  <header>
    <div class="brand"><span class="brand-dot"></span><span class="brand-name">Wablor</span></div>
    <nav class="main-nav"><a>ABOUT</a><a>HELP</a><a>CONTACT</a><a>REFUNDS</a><a>FAQ</a></nav>
    <div class="btn btn-signup">SIGNUP</div>
    <div class="btn btn-login">LOGIN</div>
  </header>

  <section class="search-band">
    <div class="search-label">FIND SOMETHING OR SOMEONE:</div>
    <div class="field" style="left:140px">mara</div>
    <div class="field" style="left:375px">in these categories...</div>
    <div class="field" style="left:609px">with these keywords</div>
    <div class="field" style="left:844px">closest to this place</div>
    <div class="search-btn">SEARCH</div>
  </section>

  <div class="map" role="img" aria-label="Street map of a city centre with roads, river and landmarks"></div>

  <aside class="results">
    <div class="results-head">SHOWING 19 OF 29 RESULTS</div>
    <div class="result">
      <h3>!MARA.LINDQVIST</h3>
      <div class="addr">24 Orchid Lane, Port Halden, Port Halden</div>
      <div class="dist"><svg width="14" height="10"><path d="M0 5h9M6 1l4 4-4 4" stroke="#34a6d7" stroke-width="2.5" fill="none"/></svg>11,545.9km - 3 months ago</div>
      <div class="instr">specific instructions</div>
      <div class="links"><span><svg width="14" height="14"><path d="M7 0l7 7-7 7-7-7z" fill="#34a6d7"/><path d="M4 7h5M7 5l2 2-2 2" stroke="#fff" stroke-width="1.3" fill="none"/></svg>Get directions</span><span><svg width="12" height="16"><path d="M6 0a6 6 0 0 1 6 6c0 4-6 10-6 10S0 10 0 6a6 6 0 0 1 6-6z" fill="#34a6d7"/><circle cx="6" cy="6" r="2.2" fill="#fff"/></svg>Show location</span></div>
    </div>
    <div class="result alt">
      <h3>!MARA.LINDQVIST</h3>
      <div class="addr">24 Orchid Lane, Port Halden, Port Halden</div>
      <div class="dist"><svg width="14" height="10"><path d="M0 5h9M6 1l4 4-4 4" stroke="#34a6d7" stroke-width="2.5" fill="none"/></svg>11,545.9km - 3 months ago</div>
      <div class="instr">specific instructions</div>
      <div class="links"><span><svg width="14" height="14"><path d="M7 0l7 7-7 7-7-7z" fill="#34a6d7"/><path d="M4 7h5M7 5l2 2-2 2" stroke="#fff" stroke-width="1.3" fill="none"/></svg>Get directions</span><span><svg width="12" height="16"><path d="M6 0a6 6 0 0 1 6 6c0 4-6 10-6 10S0 10 0 6a6 6 0 0 1 6-6z" fill="#34a6d7"/><circle cx="6" cy="6" r="2.2" fill="#fff"/></svg>Show location</span></div>
    </div>
    <div class="result">
      <h3>!MARA.LINDQVIST</h3>
      <div class="addr">24 Orchid Lane, Port Halden, Port Halden</div>
      <div class="dist"><svg width="14" height="10"><path d="M0 5h9M6 1l4 4-4 4" stroke="#34a6d7" stroke-width="2.5" fill="none"/></svg>11,545.9km - 3 months ago</div>
      <div class="instr">specific instructions</div>
      <div class="links"><span><svg width="14" height="14"><path d="M7 0l7 7-7 7-7-7z" fill="#34a6d7"/><path d="M4 7h5M7 5l2 2-2 2" stroke="#fff" stroke-width="1.3" fill="none"/></svg>Get directions</span><span><svg width="12" height="16"><path d="M6 0a6 6 0 0 1 6 6c0 4-6 10-6 10S0 10 0 6a6 6 0 0 1 6-6z" fill="#34a6d7"/><circle cx="6" cy="6" r="2.2" fill="#fff"/></svg>Show location</span></div>
    </div>
    <div class="scrollbar"><div class="scroll-thumb"></div></div>
  </aside>

  <svg class="map-pin" width="46" height="66" viewBox="0 0 46 66"><path d="M23 0a23 23 0 0 1 23 23c0 17-23 43-23 43S0 40 0 23A23 23 0 0 1 23 0z" fill="#2a9fd6"/><circle cx="23" cy="22" r="9" fill="#fff"/></svg>

  <div class="popup">
    <h3>!MARA.LINDQVIST</h3>
    <div class="addr">24 Orchid Lane, Port Halden, Port Halden</div>
    <div class="dist"><svg width="14" height="10"><path d="M0 5h9M6 1l4 4-4 4" stroke="#fff" stroke-width="2.5" fill="none"/></svg>11,545.9km - 3 months ago</div>
  </div>

  <svg class="map-controls" width="52" height="300" viewBox="0 0 52 300">
    <circle cx="24" cy="24" r="23" fill="#fff" stroke="#bbb"/>
    <path d="M24 8l-5 5h10zM24 40l-5-5h10zM8 24l5-5v10zM40 24l-5-5v10z" fill="#999"/>
    <rect x="16" y="70" width="16" height="16" fill="#fff" stroke="#bbb"/><circle cx="24" cy="78" r="3" fill="#3a86d8"/>
    <rect x="16" y="96" width="16" height="28" fill="#fff" stroke="#bbb"/><rect x="21" y="101" width="6" height="18" rx="3" fill="#f0a020"/>
    <rect x="16" y="126" width="16" height="16" fill="#fff" stroke="#bbb"/><path d="M20 134h8M24 130v8" stroke="#777" stroke-width="1.5"/>
    <rect x="22" y="142" width="4" height="128" fill="#fff" stroke="#bbb"/>
    <rect x="16" y="188" width="16" height="8" fill="#fff" stroke="#999"/>
    <rect x="16" y="280" width="16" height="16" fill="#fff" stroke="#bbb"/><path d="M20 288h8" stroke="#777" stroke-width="1.5"/>
  </svg>

  <footer>
    <nav class="footer-nav"><span>ABOUT</span><span>HELP</span><span>CONTACT</span><span>PRIVACY</span><span>TERMS</span><span>REFUNDS</span><span>FAQ</span></nav>
    <div class="copyright">COPYRIGHT 2014 &nbsp;|&nbsp; ALL RIGHTS RESERVED</div>
    <div class="social">
      <i style="background:#3b5a9a" role="img" aria-label="Social network link"></i>
      <i style="background:#2aa3db" role="img" aria-label="Social network link"></i>
      <i style="background:#f28a1b" role="img" aria-label="News feed link"></i>
      <i style="background:#c8281e" role="img" aria-label="Video channel link"></i>
    </div>
  </footer>
</div>
</body>
</html>
```